Business Card for KV

We need a double sided business card:

First Name Last Name
Cell 123-456-7890
firstname@emailaddress.com

License #1234-ABCD-4567
WFRSL # 12345
Linden County

```html
<!DOCTYPE html>
<html lang="en">
<head>
<meta charset="utf-8">
<title>KV Business Card</title>
<link href="https://fonts.googleapis.com/css2?family=Work+Sans:wght@400;500;600&display=swap" rel="stylesheet">
<style>
  :root{
    --stage:#2a2b2d;
    --navy:#2c4d68;
    --olive:#8f8d3a;
    --paper:#ffffff;
    --ink:#4a4a4a;
  }
  *{box-sizing:border-box;margin:0;padding:0}
  html,body{width:1200px;height:881px;overflow:hidden}
  body{background:var(--stage);font-family:"Work Sans",sans-serif;position:relative}
  .card{position:absolute;left:280px;width:640px;height:366px;border-radius:14px;overflow:hidden}
  .card--front{top:50px;background:var(--navy)}
  .card--back{top:465px;background:var(--paper)}

  .brand{position:absolute;display:flex;align-items:center;gap:18px}
  .brand__dot{width:58px;height:58px;border-radius:50%;background:var(--olive)}
  .brand__name{font-weight:600;font-size:64px;letter-spacing:6px;color:var(--olive);line-height:1}
  .card--front .brand{left:50%;top:50%;transform:translate(-50%,-50%)}
  .card--back .brand{left:40px;top:150px}
  .card--back .brand__dot{width:44px;height:44px}
  .card--back .brand__name{font-size:48px;color:var(--navy)}

  .wave{position:absolute;left:0;top:0;width:640px;height:200px}

  .person{position:absolute;right:40px;top:150px;text-align:right}
  .person__name{font-weight:600;font-size:24px;letter-spacing:1px;color:var(--olive)}
  .person__role{font-size:15px;color:var(--ink);margin-top:2px}
  .divider{position:absolute;left:40px;right:30px;top:222px;height:1px;background:var(--olive)}

  .contacts{position:absolute;left:40px;top:246px;list-style:none}
  .contacts li{display:flex;align-items:center;gap:10px;font-size:17px;color:var(--ink);line-height:1.6;letter-spacing:.5px}
  .contacts svg{width:12px;height:12px;fill:var(--olive);flex:none}
  .contacts .outline{fill:none;stroke:var(--olive);stroke-width:1.6}

  .license{position:absolute;right:40px;top:250px;text-align:right;font-size:16px;color:var(--ink);line-height:1.45;letter-spacing:.5px}
  .license__label{color:var(--olive);font-weight:500}
</style>
</head>
<body>
  <section class="card card--front">
    <div class="brand"><span class="brand__dot"></span><span class="brand__name">KV</span></div>
  </section>

  <section class="card card--back">
    <svg class="wave" viewBox="0 0 640 200" aria-hidden="true">
      <path d="M0 0H640V40C560 100 430 118 300 112C190 108 90 112 0 150Z" fill="var(--olive)"/>
      <path d="M0 0H640V28C560 88 430 104 300 100C190 96 90 104 0 138Z" fill="var(--paper)"/>
      <path d="M0 0H640V20C560 80 430 96 300 92C190 88 90 98 0 130Z" fill="var(--navy)"/>
    </svg>

    <div class="brand"><span class="brand__dot"></span><span class="brand__name">KV</span></div>

    <div class="person">
      <p class="person__name">DANIEL REYES</p>
      <p class="person__role">Founder</p>
    </div>

    <div class="divider"></div>

    <ul class="contacts">
      <li><svg viewBox="0 0 12 12"><path d="M2.5 0.5 4.5 3 3.4 4.4C4 6 5.8 7.8 7.6 8.6L9 7.5 11.5 9.5 10 11.5C5 11 1 7 0.5 2Z"/></svg>123-456-7890</li>
      <li><svg viewBox="0 0 12 12"><rect class="outline" x="1" y="2.5" width="10" height="7"/><path class="outline" d="M1 2.5 6 6.5 11 2.5"/></svg>info@danielreyes.com</li>
      <li><svg viewBox="0 0 12 12"><path d="M6 0.5A4 4 0 0 1 10 4.5C10 7.5 6 11.5 6 11.5S2 7.5 2 4.5A4 4 0 0 1 6 0.5ZM6 3A1.5 1.5 0 1 0 6 6 1.5 1.5 0 0 0 6 3Z"/></svg>Linden County</li>
    </ul>

    <div class="license">
      <p><span class="license__label">License</span> #1234-ABCD-4567</p>
      <p>WFRSL # 12345</p>
    </div>
  </section>
</body>
</html>
```